Implant and Mini Implant trifold brochure.

Logo is attached. Our website: www.q7zdental.com

We need an Implant and Mini Implant Flyer (on the same flyer) to be done by someone experienced in Dental marketing.

To be mailed via : Whole Route Bulk Post-Retail® (WRBP Retail®)
You need to put a Retail Indica
Reference: https://www.kelvanpost.net/business/whole-route-bulk-post.htm
Whole Route Bulk Post-Retail Indicia Guidelines

Every WRBP mailpiece must have an WRBP indicia with “ECRWSS” in the address area, within the permit indicia, or below the permit, like the examples to the right.
The WRBP Retail Indicia does not have a specific size requirement but must be larger than .5" x .5".
The type font must be in all caps and at least a 4 point size.
Place the indicia in the upper right hand corner of the mailpiece.
It should fit in the area 1.625" from the right edge and 1.375" from top edge.
Leave 1/8" of space around the top and right edge.

There should be a picture of a senior citizen eating apple - that is what implants will provide.

One side English; Other side Spanish.

If you do not have idea on what implants and mini-implants are then please ask specific questions.

Make space for specials.

Target Market(s)

dental implants, dental mini implants

Font styles to use
Other font styles liked:
• leaving it open for designer.

Colors
00a990
33b8a4
87cfc6
cadf82

Requirements
Must have
• A senior citizen eating apple - that is what implants allow people to do.
• Once the design layout is finalized, we will provide text. I am leaving the design wide open. you may look at good templates for ideas, but please respect the copyright.
Nice to have
• Use implant and mini implant pictures.
• Images needed
• 1) 3 Easy Steps to Implant Restoration in 1 visit: Use three images: mouth with missing teeth; mouth with implant screws fitted; mouth with teeth restored.
• 2) Image for Implant based Denture.
• 3) Senior Citizen or a couple eating apple.
• Image must be of good quality; even if taken from different sources they must gel well with the over all design. The final design has to be stunning.
• Please do not provide me with designs that I can get from any printing company.
• The Text area:
• 1. Why Implants?
• 2. Space for implant based dentures.
• 3. Other spaces for filling in "Why visit Q7z Dental"
• Additional Info: Time to use the following text in the final output.
• Q7z Dental - Your home for Quartz-7-Zenith Dental care.
• Q7z Dental - Your Implant Destination.
• Why Implants?
• . Durable, long lasting teeth replacement
• . Surgically implanted metal posts or frames into the jawbone
• . Allows crowns, bridges or complete dentures to be placed on implants
• Why Implant Dentures?
• . Durable and Cost Effective
• . Your denture fabricated as normal denture
• . Four or more implants are placed in one visit
• . Your denture is then retrofitted to snap on the mini implant retention head
• . Stabilize your loose dentures in one visit
• Why Mini Implants?
• . Less involved procedure than conventional implants
• . Usually completed in one dental appointment
• . Replace missing teeth instantly
• Implants vs Mini-Implants
• Visit Q7z Dental for a complementary consultation to learn which option is best for you. Depending on various conditions including that of the jawbone, you may be recommended an implant or mini-implant based treatment.
• Implant or Mini-implant treatment may not be suitable for all patients. For implants to be successful, you need to have healthy gums and adequate bones to support the implants. You must also be willing to commit to proper maintenance of your implants or dentures. Visit your dentist at Q7z Dental to learn more.
• Spanish translation from google added below:
• Q7z Dental: su casa para atención Quartz-7-Zenith dental.
• Q7z Dental: su destino de implante.
• ¿Por qué los implantes?
• . Reemplazo duradero y duradero de los dientes
• . Puestos o marcos de metal implantados quirúrgicamente en la mandíbula
• . Permiten para colocan coronas, puentes o dentaduras completas en implantes
• ¿Por qué las dentaduras postizas?
• . Durable y rentable
• . Su dentadura fabricada como dentadura normal
• . Cuatro o más implantes se colocan en una visita
• . Su dentadura se reajusta para encajar en el cabezal de retención mini implante
• . Estabilice sus dentaduras sueltas en una visita
• ¿Por qué Mini Implantes?
• . Procedimiento menos complicado que los implantes convencionales
• . Generalmente se completa en una cita dental
• . Reemplace los dientes perdidos al
• Implantes vs Mini Implantes
• Visite Q7z Dental para obtener una consulta complementaria y conocer cuál es la mejor opción para usted. Dependiendo de varias condiciones, incluida de la mandíbula, se le puede recomenda un tratamiento basado en implantes o mini-implantes.
• El tratamiento con implantes o mini-implantes puede no ser adecuado para todos los pacientes. Para que los implantes tengan éxito, debe tener encías sanas y huesos adecuados para apoyar los implantes. También debe estar dispuesto a comprometerse con el mantenimiento adecuado de sus implantes o dentaduras postizas. Visite a su dentista en Q7z Dental para obtener más información.
Should not have
• blank spaces without purpose

```html
<!DOCTYPE html>
<html lang="en">
<head>
<meta charset="utf-8">
<title>Q7z Dental – Implant &amp; Mini Implant Trifold</title>
<link href="https://fonts.googleapis.com/css2?family=Montserrat:wght@500;700;800&family=Open+Sans:wght@400;600;700&family=Yellowtail&display=swap" rel="stylesheet">
<style>
:root{
  --blue:#0c5aa6;
  --blue-deep:#08427e;
  --blue-light:#2f8fd6;
  --green:#7dc242;
  --green-deep:#4fa83a;
  --lime:#c9de3a;
  --ink:#3c4650;
  --paper:#ffffff;
  --stage:#d6d8dc;
}
*{box-sizing:border-box;margin:0;padding:0}
html,body{width:1200px;height:1194px;overflow:hidden}
body{background:var(--stage);font-family:"Open Sans",Arial,sans-serif;color:var(--ink);position:relative}
.sheet{position:absolute;left:50px;width:1100px;height:560px;display:flex;background:var(--paper);box-shadow:0 6px 18px rgba(0,0,0,.22)}
.sheet--outside{top:22px}
.sheet--inside{top:610px}
.panel{position:relative;width:366.67px;height:100%;overflow:hidden;border-right:1px solid #e3e7ea}
.panel:last-child{border-right:none}
.photo{position:absolute}
.photo-circle{position:absolute;width:84px;height:84px;border-radius:50%;border:4px solid var(--lime);box-shadow:0 2px 6px rgba(0,0,0,.2)}
.brand-name{font-family:"Montserrat",sans-serif;font-weight:700;font-size:24px;color:var(--blue);line-height:1}
.script{font-family:"Yellowtail",cursive;color:var(--blue);font-weight:400}
.head{font-family:"Montserrat",sans-serif;font-weight:800;text-transform:uppercase;line-height:1.05}
.list{list-style:none}
.list li{display:flex;align-items:center;gap:10px;font-size:11px;line-height:1.3;margin-bottom:9px}
.list svg{flex:none}
/* outside left */
.why-implants{position:absolute;left:0;top:0;width:100%;height:200px}
.why-implants .bg{position:absolute;inset:0}
.why-implants .content{position:absolute;left:26px;top:24px;right:20px;color:#fff}
.why-implants .head{color:var(--lime);font-size:19px;margin-bottom:14px}
.steps{position:absolute;left:26px;top:268px;right:18px}
.steps .head{font-size:17px;color:var(--blue)}
.steps .head em{font-style:normal;color:var(--green-deep)}
.step{display:flex;align-items:center;gap:10px;margin-top:12px}
.step-num{flex:none;width:26px;height:26px;border-radius:50%;background:var(--blue);border:2px solid var(--lime);color:#fff;font-family:"Montserrat",sans-serif;font-weight:800;font-size:13px;display:flex;align-items:center;justify-content:center}
.step-photo{flex:none;width:92px;height:56px;border-radius:28px;border:3px solid var(--lime);background:linear-gradient(180deg,#f4e8e4,#c9626a 55%,#e9dcd6)}
.step-title{font-family:"Montserrat",sans-serif;font-weight:700;font-size:11.5px;color:var(--green-deep)}
.step-text{font-size:9.5px;line-height:1.3;margin-top:2px}
/* mailing panel */
.mail-area{position:absolute;left:0;top:0;width:100%;height:250px;background:linear-gradient(180deg,#f4f5f6,#e9ecee)}
.indicia{position:absolute;right:14px;top:14px;width:92px;border:1.5px solid #333;padding:6px 4px;text-align:center;font-family:Arial,sans-serif;font-size:8px;line-height:1.35;text-transform:uppercase;color:#222;background:#fff}
.indicia b{font-size:10px}
.address{position:absolute;left:30px;top:120px;width:210px;border:1.5px solid #333;padding:10px;font-family:Arial,sans-serif;font-size:10px;line-height:1.5;color:#222;background:#fff}
.mail-swoosh{position:absolute;left:0;top:200px;width:100%;height:110px}
.mail-info{position:absolute;left:30px;right:24px;top:288px}
.mail-info p{font-size:9.5px;line-height:1.45;margin-top:6px}
.mail-info .script{font-size:18px;line-height:1.05;margin-top:8px}
.call{margin-top:8px;font-family:"Montserrat",sans-serif;font-weight:700;font-size:11px;color:var(--blue-deep);line-height:1.35}
.web-pill{position:absolute;left:24px;right:24px;bottom:22px;height:26px;border-radius:13px;background:var(--blue);color:#fff;font-size:10.5px;letter-spacing:2px;display:flex;align-items:center;justify-content:center}
/* cover */
.cover-top{position:absolute;left:24px;top:30px;right:16px}
.tagline{margin-top:18px;text-align:center}
.tagline .script{font-size:22px;display:block}
.tagline .head{font-size:17px;color:var(--green-deep);text-transform:none;font-weight:800}
.cover-photo{left:0;top:190px;width:100%;height:370px;background:linear-gradient(160deg,#cde3b0 0%,#d9c4a8 35%,#b98e6a 60%,#e6e1d6 100%)}
.cover-swoosh{position:absolute;left:0;top:168px;width:100%;height:80px}
.cover-slogan{position:absolute;left:60px;bottom:48px;color:#fff;text-shadow:0 2px 4px rgba(0,0,0,.45)}
.cover-slogan .script{color:#fff;font-size:18px}
.cover-slogan .big{font-family:"Montserrat",sans-serif;font-weight:800;font-size:30px;line-height:1}
.cover-slogan .big.indent{margin-left:38px}
/* inside left */
.family-photo{left:0;top:0;width:100%;height:250px;background:linear-gradient(180deg,#e6c9b0,#c89b7b 55%,#9fb7c8)}
.dentures{position:absolute;left:26px;right:18px;top:284px}
.dentures .head{font-size:17px;color:var(--blue)}
.dentures .head em{font-style:normal;color:var(--green-deep)}
.dentures .list{margin-top:10px}
.dentures .list li{margin-bottom:7px}
.closing{position:absolute;left:26px;right:12px;bottom:14px;text-align:center}
.closing .script{font-size:22px;display:block}
.closing .big{font-family:"Montserrat",sans-serif;font-weight:800;font-size:26px;color:var(--green-deep)}
/* inside middle */
.mini{position:absolute;left:26px;right:18px;top:30px}
.mini .head{font-size:19px;color:var(--blue)}
.mini .head em{font-style:normal;color:var(--green-deep)}
.mini .list{margin-top:16px}
.mini .list li{font-size:11.5px;margin-bottom:14px}
.mid-brand{position:absolute;left:0;right:0;top:270px;text-align:center}
.man-photo{left:0;top:350px;width:100%;height:210px;background:linear-gradient(180deg,#a9c48c,#d7b59a 50%,#f4f4f4)}
.man-curve{position:absolute;left:0;top:330px;width:100%;height:50px}
/* inside right */
.father-photo{left:0;top:0;width:100%;height:330px;background:linear-gradient(170deg,#a8c47a,#6f8a4a 40%,#3f7a4c 70%,#2a6a3a)}
.speak{position:absolute;left:20px;top:160px;color:#fff;text-shadow:0 2px 4px rgba(0,0,0,.45)}
.speak .script{color:#fff;font-size:18px}
.speak .big{font-family:"Montserrat",sans-serif;font-weight:800;font-size:24px;line-height:1.05}
.speak .big.indent{margin-left:34px}
.vs{position:absolute;left:0;top:300px;width:100%;height:260px;color:#fff}
.vs .bg{position:absolute;inset:0}
.vs .content{position:absolute;left:26px;right:20px;top:44px}
.vs .head{color:var(--lime);font-size:17px}
.vs .head small{font-size:10px;color:#fff;text-transform:lowercase}
.vs p{font-size:9.4px;line-height:1.42;margin-top:8px}
.web-pill--lime{background:var(--lime);color:var(--blue-deep);bottom:16px}
</style>
</head>
<body>

<!-- OUTSIDE -->
<section class="sheet sheet--outside">

  <article class="panel panel--flap">
    <div class="why-implants">
      <svg class="bg" viewBox="0 0 367 200" preserveAspectRatio="none" aria-hidden="true">
        <defs><linearGradient id="blueGrad" x1="0" y1="0" x2="1" y2="1"><stop offset="0" stop-color="#08427e"/><stop offset="1" stop-color="#2f8fd6"/></linearGradient></defs>
        <path d="M0 0H367V150Q200 215 0 180Z" fill="url(#blueGrad)"/>
        <path d="M0 180Q200 215 367 150V160Q200 228 0 192Z" fill="#c9de3a"/>
      </svg>
      <div class="content">
        <h2 class="head">Why Implants?</h2>
        <ul class="list">
          <li><svg width="20" height="20" viewBox="0 0 20 20"><path d="M2 9h4v9H2zM7 9l4-7c2 0 2 2 1 4h5c1 0 2 1 1 3l-2 7c0 1-1 2-2 2H7z" fill="#fff"/></svg>Durable, long lasting teeth replacement</li>
          <li><svg width="20" height="20" viewBox="0 0 20 20"><path d="M5 2v16M4 2h2M14 2c-3 0-3 5 0 5s3-5 0-5zM14 7v11" stroke="#fff" stroke-width="2" fill="none"/></svg>Surgically implanted metal posts or frames into the jawbone</li>
          <li><svg width="20" height="20" viewBox="0 0 20 20"><path d="M4 3c3-1 4 1 6 0s4-1 6 0c1 3 0 6-1 8l-1 7h-2l-1-5h-2l-1 5H6l-1-7C4 9 3 6 4 3z" fill="#fff"/></svg>Allows crowns, bridges or complete dentures to be placed on implants</li>
        </ul>
      </div>
    </div>
    <div class="photo-circle" style="left:26px;top:170px;background:linear-gradient(160deg,#d8c0a8,#9c7a62)" role="img" aria-label="Photo: smiling senior couple embracing"></div>
    <div class="photo-circle" style="left:96px;top:160px;background:linear-gradient(180deg,#e8bfa9,#f5f1ec 55%,#d79a8c)" role="img" aria-label="Photo: close-up of a bright smile"></div>
    <div class="steps">
      <h3 class="head">3 Easy Steps to <em>Implant Restoration</em> in 1 Visit:</h3>
      <div class="step">
        <span class="step-num">1</span>
        <div class="step-photo" role="img" aria-label="Photo: mouth with missing teeth"></div>
        <div><div class="step-title">Mouth with missing teeth</div><p class="step-text">Gaps make chewing hard and let nearby teeth drift out of place.</p></div>
      </div>
      <div class="step">
        <span class="step-num">2</span>
        <div class="step-photo" role="img" aria-label="Photo: mouth with implant screws fitted"></div>
        <div><div class="step-title">Mouth with implant screws fitted</div><p class="step-text">Small titanium posts are set gently into the jawbone to hold teeth.</p></div>
      </div>
      <div class="step">
        <span class="step-num">3</span>
        <div class="step-photo" role="img" aria-label="Photo: mouth with teeth restored"></div>
        <div><div class="step-title">Mouth with teeth restored</div><p class="step-text">Natural-looking crowns snap on so you can bite and smile freely.</p></div>
      </div>
    </div>
  </article>

  <article class="panel panel--mail">
    <div class="mail-area">
      <div class="indicia">PRSRT STD<br>ECRWSS<br>U.S. POSTAGE<br><b>PAID</b><br>WRBP RETAIL</div>
      <div class="address">****************ECRWSSWRBP****<br>Postal Customer<br>City, State, 5-Digit ZIP Code</div>
    </div>
    <svg class="mail-swoosh" viewBox="0 0 367 110" preserveAspectRatio="none" aria-hidden="true">
      <path d="M0 40Q120 90 367 20V110H0Z" fill="#eef6e4"/>
      <path d="M0 40Q120 90 367 20V44Q140 110 0 62Z" fill="#7dc242"/>
      <path d="M0 62Q140 110 367 44V52Q140 122 0 70Z" fill="#0c5aa6"/>
    </svg>
    <div class="mail-info">
      <div class="brand-name">Q7z Dental</div>
      <p>Your Home for "Quartz-7-Zenith Dental" Care!<br>Your local Geriatric, General &amp; Pediatric Dentistry.</p>
      <p>New Patients and Emergency Dental Appointments are Welcome.</p>
      <div class="script">We are open<br>on Saturdays!</div>
      <div class="call">CALL US TOLL FREE!<br>1-800-Q7Z-CARE<br>(1-800-555-0142)</div>
    </div>
    <div class="web-pill">www.q7zdental.com</div>
  </article>

  <article class="panel panel--cover">
    <div class="cover-top">
      <div class="brand-name" style="text-align:center">Q7z Dental</div>
      <div class="tagline"><span class="script">Your One-Stop</span><span class="head">Dental Destination.</span></div>
    </div>
    <div class="photo cover-photo" role="img" aria-label="Photo: smiling senior woman with glasses biting a green apple"></div>
    <svg class="cover-swoosh" viewBox="0 0 367 80" preserveAspectRatio="none" aria-hidden="true">
      <path d="M0 0H367V30Q180 70 0 22Z" fill="#fff"/>
      <path d="M0 22Q180 70 367 30V40Q180 82 0 32Z" fill="#7dc242"/>
      <path d="M0 32Q180 82 367 40V46Q180 90 0 38Z" fill="#0c5aa6"/>
    </svg>
    <div class="cover-slogan">
      <div class="script">So that you can smile</div>
      <div class="big">Forever</div>
      <div class="big indent">Together</div>
    </div>
  </article>
</section>

<!-- INSIDE -->
<section class="sheet sheet--inside">

  <article class="panel panel--dentures">
    <div class="photo family-photo" role="img" aria-label="Photo: happy family of four smiling together"></div>
    <svg style="position:absolute;left:0;top:200px;width:100%;height:70px" viewBox="0 0 367 70" preserveAspectRatio="none" aria-hidden="true">
      <path d="M0 50Q180 10 367 40V70H0Z" fill="#fff"/>
      <path d="M0 44Q180 4 367 34V40Q180 10 0 50Z" fill="#0c5aa6"/>
    </svg>
    <div class="photo-circle" style="left:150px;top:192px;background:linear-gradient(160deg,#d8c0a8,#9c7a62)" role="img" aria-label="Photo: smiling senior couple"></div>
    <div class="photo-circle" style="left:232px;top:186px;background:linear-gradient(180deg,#e8bfa9,#f5f1ec 55%,#d79a8c)" role="img" aria-label="Photo: close-up of a bright smile"></div>
    <div class="dentures">
      <h2 class="head"><em>Why</em><br>Implant Dentures?</h2>
      <ul class="list">
        <li><svg width="18" height="18" viewBox="0 0 20 20"><path d="M2 9h4v9H2zM7 9l4-7c2 0 2 2 1 4h5c1 0 2 1 1 3l-2 7c0 1-1 2-2 2H7z" fill="#4fa83a"/></svg>Durable and Cost Effective</li>
        <li><svg width="18" height="18" viewBox="0 0 20 20"><path d="M2 8h16v5H2z" fill="none" stroke="#4fa83a" stroke-width="2"/></svg>Your denture fabricated as normal denture</li>
        <li><svg width="18" height="18" viewBox="0 0 20 20"><path d="M4 3h12v4H4zM8 7h4v10H8z" fill="#4fa83a"/></svg>Four or more implants are placed in one visit</li>
        <li><svg width="18" height="18" viewBox="0 0 20 20"><circle cx="10" cy="10" r="8" fill="none" stroke="#4fa83a" stroke-width="2"/><path d="M6 10l3 3 5-6" stroke="#4fa83a" stroke-width="2" fill="none"/></svg>Your denture is then retrofitted to snap on the mini implant retention head</li>
        <li><svg width="18" height="18" viewBox="0 0 20 20"><path d="M4 3c3-1 4 1 6 0s4-1 6 0c1 3 0 6-1 8l-1 7h-2l-1-5h-2l-1 5H6l-1-7C4 9 3 6 4 3z" fill="none" stroke="#4fa83a" stroke-width="1.6"/></svg>Stabilize your loose dentures in one visit</li>
      </ul>
    </div>
    <div class="closing"><span class="script">You deserve nothing less...</span><span class="big">A Beautiful Smile</span></div>
  </article>

  <article class="panel panel--mini" style="background:linear-gradient(180deg,#f1f6fa,#fff 40%)">
    <div class="mini">
      <h2 class="head"><em>Why</em><br>Mini Implants?</h2>
      <ul class="list">
        <li><svg width="20" height="20" viewBox="0 0 20 20"><path d="M5 2v16M4 2h2M14 2c-3 0-3 5 0 5s3-5 0-5zM14 7v11" stroke="#4fa83a" stroke-width="2" fill="none"/></svg>Less involved procedure than conventional implants</li>
        <li><svg width="20" height="20" viewBox="0 0 20 20"><rect x="2" y="4" width="16" height="14" rx="2" fill="none" stroke="#4fa83a" stroke-width="2"/><path d="M2 8h16M6 2v4M14 2v4" stroke="#4fa83a" stroke-width="2"/></svg>Usually completed in one dental appointment</li>
        <li><svg width="20" height="20" viewBox="0 0 20 20"><path d="M4 3c3-1 4 1 6 0s4-1 6 0c1 3 0 6-1 8l-1 7h-2l-1-5h-2l-1 5H6l-1-7C4 9 3 6 4 3z" fill="none" stroke="#4fa83a" stroke-width="1.6"/></svg>Replace missing teeth instantly</li>
      </ul>
    </div>
    <div class="mid-brand"><span class="brand-name">Q7z Dental</span></div>
    <div class="photo man-photo" role="img" aria-label="Photo: smiling young man in a white shirt outdoors"></div>
    <svg class="man-curve" viewBox="0 0 367 50" preserveAspectRatio="none" aria-hidden="true">
      <path d="M0 0H367V10Q180 50 0 30Z" fill="#f7fafc"/>
      <path d="M0 30Q180 50 367 10V18Q180 60 0 38Z" fill="#0c5aa6"/>
    </svg>
  </article>

  <article class="panel panel--compare">
    <div class="photo father-photo" role="img" aria-label="Photo: smiling father giving his son a piggyback ride outdoors"></div>
    <div class="speak">
      <div class="script">Our Smiles</div>
      <div class="big">Speak For</div>
      <div class="big indent">Themselves</div>
    </div>
    <div class="photo-circle" style="left:252px;top:222px;background:linear-gradient(180deg,#e8bfa9,#f5f1ec 55%,#d79a8c)" role="img" aria-label="Photo: close-up of a bright smile"></div>
    <div class="vs">
      <svg class="bg" viewBox="0 0 367 260" preserveAspectRatio="none" aria-hidden="true">
        <defs><linearGradient id="blueGrad2" x1="0" y1="0" x2="1" y2="1"><stop offset="0" stop-color="#2f8fd6"/><stop offset="1" stop-color="#08427e"/></linearGradient></defs>
        <path d="M0 30Q180 -10 367 20V260H0Z" fill="url(#blueGrad2)"/>
        <path d="M0 22Q180 -18 367 12V20Q180 -10 0 30Z" fill="#c9de3a"/>
      </svg>
      <div class="content">
        <h2 class="head">Implants <small>vs</small><br>Mini-Implants</h2>
        <p>Visit Q7z Dental for a complementary consultation to learn which option is best for you. Depending on various conditions including that of the jawbone, you may be recommended an implant or mini-implant based treatment.</p>
        <p>Implant or Mini-implant treatment may not be suitable for all patients. For implants to be successful, you need to have healthy gums and adequate bones to support the implants. You must also be willing to commit to proper maintenance of your implants or dentures. Visit your dentist at Q7z Dental to learn more.</p>
      </div>
    </div>
    <div class="web-pill web-pill--lime">www.q7zdental.com</div>
  </article>
</section>

</body>
</html>
```